Supplier of compressed napkins looking for a label design 100mm x 70mm

Our main product, Zest-Dab, is a compressed towel/serviette that comes as a pellet of 20mm dia (1 inch) x 10mm (3/8") high. When a few drops of water are poured onto it, it grows quickly and is then unrolled by the user to wipe their hands or face, or golf clubs or fishing equipment or when camping. See video on landing page of www.foldedmarvel.example and the how to use video on the Applications page.
The label should also act as a sleeve in which 10 of these will be wrapped for consumer display and sale. The logo for the company is attached, but I would also like a logo for the ZEST-DAB name.
The product also comes in boxes of 100 and 500 wipes, for bulk purchasers like restaurants.
Target Market(s)
Higher end restaurants, and those serving finger foods (bbq, fried chicken, etc.)
Spas (much cheaper than having clients use nice towels to remove makeup and nail polish.)
Golf courses (to clean golf clubs, and to refresh golfers after a round).
Campers (easy way to clean up hands and face when camping).
Baby care (clean up when changing diaper).
Fishermen (easy to clean up after catching a fish, unhooking it, gutting it, etc.)
Travelers---auto, airplane, rail, bus.
Industry/Entity Type
Cleaning Product
Font styles to use
Requirements
Must have
- The word ZEST-DAB as the product name.
- Manufactured for: Folded Marvel Inc. Add FM logo attached.
- 1-844-555-0137
- These wipes are 100% recyclable and environmentally friendly, so reference or mention of this is key.
- 100% Cellulose.
- Each wipe measures 24cm x 24cm (10" x 10") when unrolled.
- Directions for use: Add a few drops of water, let expand, unroll, and use.
- Contains no additives, chemicals or preservatives.
- Warning: Not to be swallowed! Keep out of the reach of young children.
- Made in Canada
Nice to have
- The sleeve/label will be round, and so needs to be easy to read like this.
- Think of the candy roll Tin Rafts, and how they made that label (without all of the colors, of course). Or Quelbix.

```html
<!DOCTYPE html>
<html lang="en">
<head>
<meta charset="utf-8">
<title>Zest-Dab Label</title>
<link rel="stylesheet" href="https://fonts.googleapis.com/css2?family=Arimo:wght@400;700&display=swap">
<style>
:root{
  --sky:#bfe3f7;
  --sky-deep:#7cc4ec;
  --mist:#eaf6fd;
  --panel:#d8eef9;
  --icon:#79b8e2;
  --brand:#2b9fdc;
  --ink:#1c1c1c;
  --white:#ffffff;
  --navy:#143c78;
}
*{margin:0;padding:0;box-sizing:border-box}
html,body{width:839px;height:1200px;overflow:hidden;background:var(--white)}
body{font-family:"Arimo",Arial,sans-serif;color:var(--ink)}
.label{position:relative;width:839px;height:1200px;overflow:hidden;
  background:linear-gradient(180deg,var(--sky) 0%,var(--mist) 26%,var(--white) 34%,var(--white) 62%,var(--mist) 80%,var(--sky) 100%)}
.facets{position:absolute;inset:0}
.abs{position:absolute}
.brand-mark{left:39px;top:71px;width:58px;height:58px;border-radius:50%;background:var(--white);
  display:flex;align-items:center;justify-content:center;font-size:21px;font-weight:700;color:var(--ink)}
.count-ribbon{left:668px;top:100px;width:110px;height:64px}
.product-name{left:0;right:0;top:178px;text-align:center;font-size:96px;font-weight:700;color:var(--brand);letter-spacing:4px}
.tagline{left:118px;top:283px;width:603px;height:46px;border-radius:23px;background:var(--white);
  display:flex;align-items:center;justify-content:center;font-size:22px}
.eco-icons{left:684px;top:388px;width:110px;height:52px}
.web{left:62px;top:529px;font-size:15px}
.maker-mark{left:362px;top:456px;font-size:44px;font-weight:400;color:var(--ink)}
.maker{left:467px;top:460px;font-size:22px;line-height:30px}
.maker strong{font-weight:700}
.phone{left:30px;top:578px;font-size:22px}
.price-box{left:30px;top:620px;width:316px;height:136px;border:1.5px solid var(--ink);border-radius:14px;
  padding:14px 20px;font-size:21px;line-height:37px}
.directions-title{left:368px;top:568px;font-size:18px;font-weight:700}
.directions{left:368px;top:597px;width:430px;height:160px;background:var(--panel);border-radius:10px;display:flex;padding:10px 0}
.step{flex:1;text-align:center;font-size:15px;line-height:20px;border-right:1.5px solid var(--white);display:flex;flex-direction:column;align-items:center}
.step:last-child{border-right:none}
.step svg{width:80px;height:90px;margin-bottom:4px}
.copy{left:30px;top:795px;width:780px;font-size:21px;line-height:28px}
.copy p{margin-bottom:8px}
.copy b{font-weight:700}
.warning{left:30px;top:995px;width:760px;height:46px;border:1.5px solid var(--ink);
  display:flex;align-items:center;justify-content:center;font-size:21px}
.warning b{margin-right:6px}
.origin{left:30px;top:1075px;font-size:22px}
</style>
</head>
<body>
<div class="label">
  <svg class="facets" viewBox="0 0 839 1200" aria-hidden="true">
    <polygon points="0,0 300,0 0,330" fill="#ffffff" opacity=".25"/>
    <polygon points="520,0 839,0 839,260" fill="#ffffff" opacity=".3"/>
    <polygon points="180,0 560,0 260,360" fill="#9fd4f2" opacity=".2"/>
    <polygon points="0,900 320,1200 0,1200" fill="#9fd4f2" opacity=".35"/>
    <polygon points="600,880 839,720 839,1200 520,1200" fill="#ffffff" opacity=".3"/>
    <polygon points="300,1200 560,960 700,1200" fill="#8ccbef" opacity=".25"/>
  </svg>

  <div class="abs brand-mark">FM</div>

  <svg class="abs count-ribbon" viewBox="0 0 110 64" aria-label="10 wipes">
    <text x="55" y="30" text-anchor="middle" font-family="Arimo, Arial, sans-serif" font-weight="700" font-size="30" fill="#143c78">10</text>
    <path d="M6 40 Q55 28 104 40 L100 58 Q55 46 10 58 Z" fill="#2b9fdc"/>
    <text x="55" y="53" text-anchor="middle" font-family="Arimo, Arial, sans-serif" font-weight="700" font-size="12" fill="#fff">WIPES</text>
  </svg>

  <div class="abs product-name">ZEST-DAB</div>
  <div class="abs tagline"><span><b>100%</b>&nbsp;recyclable and environmentally friendly wipes.</span></div>

  <svg class="abs eco-icons" viewBox="0 0 110 52" aria-label="Recyclable and earth friendly">
    <g fill="none" stroke="#1c1c1c" stroke-width="2">
      <path d="M24 6 L36 26 M36 26 L30 25 M36 26 L38 20"/>
      <path d="M42 40 L8 40 M8 40 L12 36 M8 40 L12 44"/>
      <path d="M6 34 L20 10 M20 10 L14 12 M20 10 L22 16"/>
      <circle cx="84" cy="20" r="14"/>
      <path d="M70 20 H98 M84 6 C76 14 76 26 84 34 M84 6 C92 14 92 26 84 34"/>
      <path d="M66 36 Q72 48 84 48 Q96 48 102 36"/>
    </g>
  </svg>

  <div class="abs web">www.foldedmarvel.example</div>

  <div class="abs maker-mark">FM</div>
  <div class="abs maker">Manufactured for:<br><strong>FOLDED MARVEL Inc.</strong></div>

  <div class="abs phone">1-844-555-0137</div>
  <div class="abs price-box">Price:<br>Mfg. Date:<br>Exp. Date:</div>

  <div class="abs directions-title">Directions for use:</div>
  <div class="abs directions">
    <div class="step">
      <svg viewBox="0 0 80 90" aria-hidden="true">
        <circle cx="40" cy="62" r="24" fill="var(--icon)"/>
        <path d="M40 8 Q46 20 40 26 Q34 20 40 8Z" fill="#fff" stroke="#1c1c1c" stroke-width="1.5"/>
        <ellipse cx="40" cy="58" rx="13" ry="5" fill="#fff" stroke="#1c1c1c" stroke-width="1.5"/>
        <path d="M27 58 V64 Q40 72 53 64 V58" fill="#fff" stroke="#1c1c1c" stroke-width="1.5"/>
      </svg>
      <span>Add a few<br>drops of water</span>
    </div>
    <div class="step">
      <svg viewBox="0 0 80 90" aria-hidden="true">
        <circle cx="40" cy="62" r="24" fill="var(--icon)"/>
        <rect x="29" y="8" width="22" height="66" rx="11" fill="#fff" stroke="#1c1c1c" stroke-width="1.5"/>
        <ellipse cx="40" cy="14" rx="4" ry="2" fill="none" stroke="#1c1c1c" stroke-width="1.5"/>
      </svg>
      <span>Let it<br>expand</span>
    </div>
    <div class="step">
      <svg viewBox="0 0 80 90" aria-hidden="true">
        <circle cx="40" cy="62" r="24" fill="var(--icon)"/>
        <path d="M10 12 H62 V64 Q40 58 14 66 Z" fill="#fff" stroke="#1c1c1c" stroke-width="1.5"/>
        <rect x="56" y="10" width="14" height="56" rx="7" fill="#fff" stroke="#1c1c1c" stroke-width="1.5"/>
      </svg>
      <span>Unroll it</span>
    </div>
    <div class="step">
      <svg viewBox="0 0 80 90" aria-hidden="true">
        <circle cx="40" cy="62" r="24" fill="var(--icon)"/>
        <path d="M14 16 Q40 8 68 14 Q62 36 66 58 Q40 52 16 60 Q20 38 14 16Z" fill="#fff" stroke="#1c1c1c" stroke-width="1.5"/>
      </svg>
      <span>Use it</span>
    </div>
  </div>

  <div class="abs copy">
    <p>These wipes are 100% recyclable and environmentally friendly</p>
    <p><b>Material:</b> 100% Cellulose, Super Absorbent, Soft and Durable, Environment friendly, 100% Biodegradable, Suitable for all skin types &amp; Contains no additives, chemicals or preservatives.</p>
    <p><b>Specifications:</b> <b>Size:</b> 24 x 24 cm (unrolled), <b>Shape:</b> Round, <b>Color:</b> White</p>
  </div>

  <div class="abs warning"><b>Warning:</b> Not to be swallowed! Keep out of the reach of young children.</div>
  <div class="abs origin">Made in Canada</div>
</div>
</body>
</html>
```